Infectious Diseases Research Laboratory Needs Business Card

We need a business card for an academic research laboratory based in Kansas City called MORVEK. The full lab name is Microbial Dose-Response/Exposure Bridging Studies Laboratory, but this does not need to be incorporated. We study novel ways to optimize the treatment of multidrug-resistant bacterial infections ("superbugs") throughout the entire biomedical research spectrum (from benchtop to bedside). The name MORVEK is not only an acronym for our lab name, but also represents our desire to make discoveries and explore the unknown (the stars, if you well). It also serves as an ode to the state of Kansas motto where we are based, ad astra per aspera ("to the stars, through difficulty").

Target Market(s)

Pharmaceutical companies, researchers

Industry/Entity Type

Pharmaceutical

Contact Information for Business Card

The business card should incorporate and complement our new logo (see uploaded files). Double-sided designs are preferred. Looking for something modern, but professional.

Font styles to use
Sans Serif

Requirements
Must have
• Double-sided. One side would ideally be a solid color incorporating logo and the other should also have the logo (smaller), but incorporate staff information.
• Color codes:
• Red: #F04C51
• Blue: #3477B5
• Gray: #808285

```html
<!DOCTYPE html>
<html lang="en">
<head>
<meta charset="utf-8">
<title>MORVEK Business Card</title>
<link href="https://fonts.googleapis.com/css2?family=Source+Sans+3:wght@300;400;600&display=swap" rel="stylesheet">
<style>
  :root {
    --backdrop: #2f2926;
    --card: #0d0d0e;
    --red: #F04C51;
    --blue: #3477B5;
    --gray: #808285;
    --silver: #c9cacc;
    --white: #f2f2f2;
  }
  * { margin: 0; padding: 0; box-sizing: border-box; }
  html, body {
    width: 1200px; height: 900px; overflow: hidden;
    background: var(--backdrop);
    font-family: "Source Sans 3", "Helvetica Neue", Arial, sans-serif;
  }
  .stage {
    width: 1200px; height: 900px;
    display: flex; align-items: center; justify-content: center; gap: 40px;
  }
  .card {
    width: 540px; height: 309px;
    background: var(--card);
    position: relative;
    box-shadow: 0 12px 30px rgba(0,0,0,.45);
  }
  /* Info side */
  .card--info .brand-zone {
    position: absolute; left: 0; top: 0; width: 250px; height: 100%;
    display: flex; align-items: center; justify-content: center; gap: 10px;
  }
  .brand-dot { width: 14px; height: 14px; border-radius: 50%; background: var(--red); }
  .brand-name {
    color: var(--white); font-weight: 400; font-size: 30px; letter-spacing: 4px;
  }
  .divider {
    position: absolute; left: 262px; top: 78px; width: 1px; height: 150px;
    background: var(--red); opacity: .6;
  }
  .details {
    position: absolute; left: 284px; top: 70px; color: var(--white);
  }
  .person-name {
    font-size: 21px; font-weight: 600; letter-spacing: .5px; line-height: 1;
    text-transform: uppercase;
  }
  .person-name .first { color: var(--red); }
  .person-name .last { color: var(--blue); }
  .person-role { font-size: 14px; font-weight: 400; margin-top: 3px; }
  .contact-list { list-style: none; margin-top: 12px; }
  .contact-list li {
    display: flex; align-items: center; gap: 8px;
    font-size: 14.5px; line-height: 21px;
  }
  .contact-list svg { width: 10px; height: 10px; fill: var(--red); flex: none; }
  .address { font-size: 14.5px; line-height: 20px; margin-top: 12px; }
  /* Logo side */
  .card--logo {
    display: flex; align-items: center; justify-content: center; gap: 16px;
  }
  .card--logo .brand-dot { width: 22px; height: 22px; background: var(--silver); }
  .card--logo .brand-name {
    color: var(--silver); font-size: 46px; font-weight: 300; letter-spacing: 6px;
  }
</style>
</head>
<body>
<main class="stage">
  <section class="card card--info" aria-label="Business card, contact side">
    <div class="brand-zone">
      <span class="brand-dot"></span>
      <span class="brand-name">MORVEK</span>
    </div>
    <div class="divider"></div>
    <div class="details">
      <h1 class="person-name"><span class="first">Daniel</span> <span class="last">Harlow</span></h1>
      <p class="person-role">Managing Director</p>
      <ul class="contact-list">
        <li><svg viewBox="0 0 10 10"><path d="M2 0.5 L3.6 2.8 L2.7 3.8 Q3.8 6.2 6.2 7.3 L7.2 6.4 L9.5 8 L8.4 9.5 Q1 8 0.5 1.6 Z"/></svg>(816)555-0142</li>
        <li><svg viewBox="0 0 10 10"><path d="M0 2 H10 V8.5 H0 Z M0.6 2.4 L5 5.6 L9.4 2.4" stroke="#0d0d0e" stroke-width="0.8"/></svg>info@morveklab.org</li>
        <li><svg viewBox="0 0 10 10"><circle cx="5" cy="5" r="4.8"/></svg>www.morveklab.org</li>
      </ul>
      <p class="address">4800 Research Way,<br>Kansas City, 64110</p>
    </div>
  </section>
  <section class="card card--logo" aria-label="Business card, brand side">
    <span class="brand-dot"></span>
    <span class="brand-name">MORVEK</span>
  </section>
</main>
</body>
</html>
```